Management consulting Company in the electronic payment ecosystem needs a Website

We need to have a "showcase" style website that contains the key message that our company is able to provide management consulting in the world of payment systems. Our mission is to assist our clients in reviewing their sales, purchasing, operation and IT processes and to support them in identifying the best solution in the use of payment systems.

```html
<!DOCTYPE html>
<html lang="en">
<head>
<meta charset="utf-8">
<title>Orvane Consulting</title>
<link href="https://fonts.googleapis.com/css2?family=Montserrat:wght@400;500;600;700;800&family=Arimo:wght@400&display=swap" rel="stylesheet">
<style>
:root{
  --navy:#121b58;
  --navy-deep:#0d1447;
  --grey:#4b4b4d;
  --white:#ffffff;
  --body:#555a66;
  --hero-a:#3b3f4a;
  --hero-b:#6b6e74;
}
*{margin:0;padding:0;box-sizing:border-box}
html,body{width:1200px;height:3219px;overflow:hidden;background:var(--white)}
body{position:relative;font-family:'Montserrat',sans-serif}
.abs{position:absolute}
.shapes{position:absolute;left:0;top:0}
.hero-photo{left:0;top:0;width:1200px;height:790px;background:linear-gradient(120deg,var(--hero-b),var(--hero-a) 55%,#5a5650)}
.brand{color:var(--white);font-weight:700;display:flex;align-items:center;gap:12px}
.brand .dot{width:58px;height:58px;border:7px solid var(--white);border-radius:50%}
.brand-top{left:112px;top:36px;font-size:46px}
.nav{top:56px;left:462px;display:flex;font-size:15px;font-weight:600;color:var(--white)}
.nav a{color:inherit;text-decoration:none;padding:9px 16px;margin-right:8px;border:1.5px solid transparent;border-radius:2px}
.nav a.active{border-color:var(--white)}
.hero-title{left:0;width:1200px;top:405px;text-align:center;color:var(--white);font-size:80px;font-weight:800;letter-spacing:1px}
.hero-sub{left:0;width:1200px;top:508px;text-align:center;color:var(--white);font-size:22px;font-weight:600;line-height:39px}
.mission-photo{left:112px;top:852px;width:425px;height:425px;border-radius:50%;background:radial-gradient(circle at 55% 45%,#5a6aa8,#2e3a7c 70%)}
.h2{color:var(--navy);font-weight:600;font-size:35px}
.mission-title{left:594px;top:860px}
.copy{font-family:'Arimo',sans-serif;color:var(--body);font-size:15.5px;line-height:30px;text-align:justify}
.mission-copy{left:597px;top:928px;width:484px}
.mission-copy p{margin-bottom:30px}
.btn{left:597px;top:1196px;width:138px;height:50px;background:var(--navy);color:var(--white);font-size:16px;font-weight:600;display:flex;align-items:center;justify-content:center;border-radius:2px}
.services-title{left:0;width:1200px;top:1485px;text-align:center;color:var(--white);font-weight:600;font-size:34px}
.services-intro{left:250px;width:700px;top:1541px;text-align:center;color:var(--white);font-family:'Arimo',sans-serif;font-size:16px;line-height:30px}
.service{width:300px;text-align:center;color:var(--white)}
.service .icon{width:140px;height:140px;margin:0 auto;border-radius:50%;background:var(--white);border:4px solid var(--white);box-shadow:inset 0 0 0 4px var(--navy);display:flex;align-items:center;justify-content:center}
.service h3{font-weight:600;font-size:23px;margin:22px 0 10px}
.service p{font-family:'Arimo',sans-serif;font-size:14px;line-height:26px;opacity:.9;width:264px;margin:0 auto}
.why-photo{left:112px;top:2190px;width:492px;height:437px;background:linear-gradient(135deg,#8fb5cf,#4d7fa5 50%,#cfe0ea)}
.why-card{left:521px;top:2294px;width:560px;height:415px;background:var(--white);box-shadow:0 4px 18px rgba(0,0,0,.15)}
.why-title{left:565px;top:2344px}
.why-rule{left:565px;top:2402px;width:62px;height:3px;background:var(--navy)}
.why-copy{left:565px;top:2423px;width:480px}
.brand-foot{left:130px;top:2890px;font-size:64px}
.brand-foot .dot{width:86px;height:86px;border-width:9px}
.divider{width:1px;height:125px;background:rgba(255,255,255,.25);top:2890px}
.foot-text{color:var(--white);font-size:16px;line-height:23px;font-weight:500}
.social{width:42px;height:42px;border:2px solid var(--white);border-radius:50%;top:2980px}
.foot-line{left:112px;top:3075px;width:978px;height:1px;background:rgba(255,255,255,.2)}
.foot-nav{left:0;width:1200px;top:3114px;display:flex;justify-content:center;gap:40px;color:var(--white);font-size:15px;font-weight:600}
.copyright{left:0;width:1200px;top:3159px;text-align:center;color:var(--white);font-size:16px;font-weight:500}
</style>
</head>
<body>
<div class="abs hero-photo" role="img" aria-label="Photo of a business team meeting around a table"></div>

<svg class="shapes" width="1200" height="3219" viewBox="0 0 1200 3219">
  <polygon points="795,727 1200,748 1200,790" fill="var(--grey)"/>
  <polygon points="0,783 795,727 1200,773 1200,1380 0,1380" fill="var(--white)"/>
  <polygon points="0,1400 300,1432 0,1475" fill="var(--grey)"/>
  <polygon points="0,1475 1200,1312 1200,1962 0,2130" fill="var(--navy)"/>
  <polygon points="1200,1962 1000,1990 1200,2050" fill="var(--grey)"/>
  <polygon points="0,2745 790,2822 1200,2765 1200,3219 0,3219" fill="var(--grey)"/>
  <polygon points="790,2822 1200,2765 1200,2862" fill="var(--navy-deep)"/>
</svg>

<div class="abs brand brand-top"><span class="dot"></span>Orvane</div>
<nav class="abs nav">
  <a class="active">HOME</a><a>ABOUT US</a><a>SERVICES</a><a>MISSION</a><a>NEWS</a><a>CONTACT US</a>
</nav>
<h1 class="abs hero-title">ORVANE CONSULTING</h1>
<p class="abs hero-sub">SED UT PERSPICIATIS UNDE OMNIS ISTE NATUS ERROR SIT<br>VOLUPTATEM ACCUSANTIUM DOLOREMQUE</p>

<div class="abs mission-photo" role="img" aria-label="Circular photo of consultants at work, tinted blue"></div>
<h2 class="abs h2 mission-title">OUR MISSION</h2>
<div class="abs copy mission-copy">
  <p>Our mission is to assist our clients in reviewing their sales purchasing, operation and IT processes and to support them in identifying the best solution in the use of payment systems.</p>
  <p>Sed ut perspiciatis unde omnis iste natus error sit voluptatem accusa ntium doloremque laudantium, totam rem aperiam, eaque ipsa quaeab illo inventore veritatis et quasi architecto beatae vitae dicta sunt enim ipsam voluptatem quia voluptas explicabo.</p>
</div>
<div class="abs btn">READ MORE</div>

<h2 class="abs services-title">OUR SERVICES</h2>
<p class="abs services-intro">Sed ut perspiciatis unde omnis iste natus error sit voluptatem accusa ntium doloremque totam rem aperiam, eaque ipsa quaeab illo inventore veritatis</p>

<div class="abs service" style="left:118px;top:1648px">
  <div class="icon"><svg width="80" height="60" viewBox="0 0 80 60" fill="none" stroke="var(--navy)" stroke-width="3"><circle cx="12" cy="12" r="5"/><circle cx="68" cy="12" r="5"/><circle cx="40" cy="14" r="4"/><circle cx="30" cy="6" r="3"/><circle cx="50" cy="6" r="3"/><path d="M4 30h16v20M60 50V30h16M22 36h36M28 36v18M52 36v18"/></svg></div>
  <h3>SERVICES 01</h3>
  <p>Sed ut perspiciatis unde omnis iste natus error sit voluptatem accusa ntium dolorem totam rem aperiam, eaque</p>
</div>
<div class="abs service" style="left:453px;top:1648px">
  <div class="icon"><svg width="70" height="66" viewBox="0 0 70 66" fill="none" stroke="var(--navy)" stroke-width="3"><rect x="4" y="14" width="54" height="48"/><rect x="30" y="2" width="36" height="24" fill="var(--white)"/><path d="M36 10h24M36 17h18"/><circle cx="20" cy="36" r="6"/><path d="M10 54c2-8 18-8 20 0"/></svg></div>
  <h3>SERVICES 02</h3>
  <p>Sed ut perspiciatis unde omnis iste natus error sit voluptatem accusa ntium dolorem totam rem aperiam, eaque</p>
</div>
<div class="abs service" style="left:787px;top:1648px">
  <div class="icon"><svg width="80" height="66" viewBox="0 0 80 66" fill="none" stroke="var(--navy)" stroke-width="3"><rect x="18" y="2" width="44" height="26"/><path d="M26 10h28M26 18h28"/><circle cx="20" cy="42" r="5"/><circle cx="40" cy="42" r="5"/><circle cx="60" cy="42" r="5"/><path d="M8 62c2-10 22-10 24 0M28 62c2-10 22-10 24 0M48 62c2-10 22-10 24 0"/></svg></div>
  <h3>SERVICES 03</h3>
  <p>Sed ut perspiciatis unde omnis iste natus error sit voluptatem accusa ntium dolorem totam rem aperiam, eaque</p>
</div>

<div class="abs why-photo" role="img" aria-label="Photo of colleagues reviewing plans at a bright office table"></div>
<div class="abs why-card"></div>
<h2 class="abs h2 why-title">WHY CHOOSE US</h2>
<div class="abs why-rule"></div>
<p class="abs copy why-copy">Sed ut perspiciatis unde omnis iste natus error sit voluptatem accus antium doloremque laudantium, totam rem aperiam, eaque ipsa quae ab illo inventore veritatis et quasi architecto beatae vitae dicta sunt explicabo. Nemo enim ipsam voluptatem quia voluptas sit aspernatur aut odit aut fugit, sed quia consequuntur magni dolores eos qui ratione voluptatem sequi nesciunt. Neque porro adipisci velit, sed quia non numquam eius modi unde omnis iste natus error sit voluptatem accus antium doloremque laudantium</p>

<div class="abs brand brand-foot"><span class="dot"></span>Orvane</div>
<div class="abs divider" style="left:446px"></div>
<svg class="abs" style="left:490px;top:2905px" width="22" height="26" viewBox="0 0 22 26" fill="none" stroke="var(--white)" stroke-width="1.6"><path d="M11 25C5 17 2 13 2 9a9 9 0 0 1 18 0c0 4-3 8-9 16z"/><circle cx="11" cy="9" r="3"/></svg>
<div class="abs foot-text" style="left:530px;top:2900px">Address<br>P.O. Box 741 Harlow Street<br>Brenton MA 02196</div>
<div class="abs social" style="left:530px"></div>
<div class="abs social" style="left:583px"></div>
<div class="abs divider" style="left:776px"></div>
<svg class="abs" style="left:830px;top:2912px" width="22" height="22" viewBox="0 0 22 22" fill="none" stroke="var(--white)" stroke-width="1.6"><path d="M5 2l4 5-2 3c1 3 3 5 6 6l3-2 5 4-3 3C10 20 2 12 2 5z"/></svg>
<div class="abs foot-text" style="left:868px;top:2900px">Phone:<br>000-555-0148</div>
<svg class="abs" style="left:830px;top:2972px" width="24" height="18" viewBox="0 0 24 18" fill="none" stroke="var(--white)" stroke-width="1.6"><rect x="1" y="1" width="22" height="16"/><path d="M1 1l11 9 11-9"/></svg>
<div class="abs foot-text" style="left:870px;top:2968px">Email:<br>hello@orvanemail.com</div>
<div class="abs foot-line"></div>
<div class="abs foot-nav"><span>HOME</span><span>ABOUT US</span><span>SERVICES</span><span>MISSION</span><span>NEWS</span><span>CONTACT US</span></div>
<div class="abs copyright">Orvane Consulting © 2021.All Rights Reserved.</div>
</body>
</html>
```